Coral Beacon Stationery Design Project

I am looking for a suitable stationary design for my company Coral Beacon Pty Ltd (ACN 582 914 306).

The requirements can be better explained by visiting my website
"coral-beacon-trust.org"

I will be sending letters to Ministers of State and the Heads of Government Agencies so the theme needs to be formal and serious.

A theme with a shield or similar picking on the "guardian" concept would be appropriate

Target Market(s)

Ministers of State and Department Agency Heads and legal firms, the heads of Trustee Companies as well as Members of Coral Beacon

Industry/Entity Type

Government

Requirements
Must have
• Letterhead design is a priority - Business Card secondary

Must include tag line "Steady hands for every estate we tend" with a registered trade mark superscript at the end that is an R in a circle {Windows Alt +0174 on numeric keypad or Mac Option +R}.

Must include website address "Coral-Beacon-Trust.org" plus Email address "corbeacon@mailvessel.net

Company name "Coral Beacon Pty. Ltd." and Australian Company Number "ACN 582 914 306" needs to be shown more discretely

Address is "47 Finch Crescent, Marrowdale, 3291"
Nice to have
• A watermark is something to be considered

```html
<!DOCTYPE html>
<html lang="en">
<head>
<meta charset="utf-8">
<title>Coral Beacon Stationery</title>
<link rel="stylesheet" href="https://fonts.googleapis.com/css2?family=Arimo:wght@400;700&family=Open+Sans:wght@400;600&display=swap">
<style>
  :root {
    --backdrop: #e4e1dc;
    --paper: #ffffff;
    --paper-shade: #f1f1f1;
    --ink: #1c1c1c;
    --ink-soft: #4a4a4a;
    --gold: #b8901c;
    --gold-light: #e9cf6a;
    --gold-dark: #8a6410;
    --rule: #2a2a2a;
    --wash-light: #f4f1e9;
    --wash-dark: #e6e1d3;
  }
  * { margin: 0; padding: 0; box-sizing: border-box; }
  html, body { width: 1200px; height: 1013px; overflow: hidden; }
  body {
    background: var(--backdrop);
    font-family: "Arimo", Arial, sans-serif;
    color: var(--ink);
    position: relative;
  }

  .sheet {
    position: absolute;
    top: 75px;
    width: 483px;
    height: 624px;
    background: linear-gradient(180deg, var(--paper) 0%, var(--paper-shade) 100%);
    box-shadow: 0 2px 6px rgba(0,0,0,.25);
  }
  .sheet--watermark { left: 105px; }
  .sheet--banded { left: 636px; }

  .brand { position: absolute; display: flex; align-items: center; gap: 6px; }
  .brand__mark {
    width: 26px; height: 26px;
    background: var(--gold);
    flex: none;
  }
  .brand__text { line-height: 1; }
  .brand__name { font-size: 17px; font-weight: 400; color: var(--ink); white-space: nowrap; }
  .brand__tagline { font-size: 10px; color: var(--gold); margin-top: 3px; white-space: nowrap; }
  .brand__tagline sup { font-size: 6px; }

  .sheet--watermark .brand { top: 20px; left: 112px; }
  .watermark {
    position: absolute;
    left: 161px; top: 212px;
    width: 164px; height: 198px;
    background: radial-gradient(ellipse at 50% 45%, var(--wash-light) 0%, var(--wash-dark) 100%);
    opacity: .7;
  }
  .footer-line {
    position: absolute; left: 0; right: 0;
    text-align: center; font-size: 7px; color: var(--ink-soft);
    white-space: nowrap;
  }
  .footer-line--contact { top: 596px; }
  .footer-line--acn { top: 610px; }
  .sep { display: inline-block; width: 1px; height: 8px; background: #999; margin: 0 5px; vertical-align: middle; }
  .dot { display: inline-block; width: 4px; height: 4px; background: var(--ink); margin-right: 3px; vertical-align: middle; }

  .sheet--banded .brand { top: 20px; left: 59px; }
  .contact-block {
    position: absolute; top: 24px; left: 355px;
    padding-left: 6px; border-left: 1px solid #bbb;
    font-size: 6.5px; line-height: 11px; color: var(--ink-soft);
    white-space: nowrap;
  }
  .contact-block .gap { height: 4px; }
  .gold-band {
    position: absolute; left: 0; right: 0; bottom: 0;
    height: 23px;
    background: linear-gradient(90deg, var(--gold-dark) 0%, var(--gold-light) 30%, var(--gold) 60%, var(--gold-light) 85%, var(--gold-dark) 100%);
    border-top: 3px solid var(--paper);
    box-shadow: 0 -2px 0 var(--rule);
    text-align: center; font-size: 6.5px; line-height: 20px; color: var(--paper);
  }

  .option-label {
    position: absolute; top: 716px;
    font-family: "Open Sans", Arial, sans-serif;
    font-size: 34px; color: var(--ink);
    width: 483px; text-align: center;
  }
  .option-label--one { left: 90px; }
  .option-label--two { left: 622px; }

  .card {
    position: absolute; top: 815px;
    width: 256px; height: 146px;
    background: linear-gradient(180deg, var(--paper) 0%, var(--paper-shade) 100%);
    border-radius: 8px;
    overflow: hidden;
    box-shadow: 0 2px 5px rgba(0,0,0,.25);
  }
  .card--front { left: 336px; }
  .card--back { left: 627px; }
  .card .brand__mark { width: 22px; height: 22px; }
  .card .brand__name { font-size: 14px; }
  .card .brand__tagline { font-size: 8px; }
  .card--front .brand { top: 25px; left: 19px; }
  .card__contact {
    position: absolute; top: 100px; left: 0; right: 0;
    display: flex; justify-content: center; gap: 6px;
    font-size: 6.5px; line-height: 9px; color: var(--ink-soft);
    white-space: nowrap;
  }
  .card__address { text-align: right; padding-right: 6px; border-right: 1px solid #bbb; }
  .card .gold-band { height: 20px; line-height: 17px; }
  .card--back .brand { top: 53px; left: 22px; }
  .card__url {
    position: absolute; top: 119px; left: 0; right: 0;
    text-align: center; font-size: 7px; letter-spacing: 1.5px; color: var(--ink-soft);
  }
</style>
</head>
<body>

<section class="sheet sheet--watermark">
  <div class="brand">
    <span class="brand__mark"></span>
    <div class="brand__text">
      <div class="brand__name">Coral Beacon Pty Ltd.</div>
      <div class="brand__tagline">Steady hands for every estate we tend<sup>®</sup></div>
    </div>
  </div>
  <div class="watermark" role="img" aria-label="Faint watermark area in pale gold"></div>
  <div class="footer-line footer-line--contact">
    47 Finch Crescent, Marrowdale, 3291<span class="sep"></span><span class="dot"></span>corbeacon@mailvessel.net &nbsp; <span class="dot"></span>www.Coral-Beacon-Trust.org
  </div>
  <div class="footer-line footer-line--acn">ACN 582 914 306</div>
</section>

<section class="sheet sheet--banded">
  <div class="brand">
    <span class="brand__mark"></span>
    <div class="brand__text">
      <div class="brand__name">Coral Beacon Pty Ltd.</div>
      <div class="brand__tagline">Steady hands for every estate we tend<sup>®</sup></div>
    </div>
  </div>
  <div class="contact-block">
    <div>47 Finch Crescent, Marrowdale, 3291</div>
    <div class="gap"></div>
    <div><span class="dot"></span>corbeacon@mailvessel.net</div>
    <div><span class="dot"></span>www.Coral-Beacon-Trust.org</div>
  </div>
  <div class="gold-band">ACN 582 914 306</div>
</section>

<div class="option-label option-label--one">Option-1</div>
<div class="option-label option-label--two">Option-2</div>

<section class="card card--front">
  <div class="brand">
    <span class="brand__mark"></span>
    <div class="brand__text">
      <div class="brand__name">Coral Beacon Pty Ltd.</div>
      <div class="brand__tagline">Steady hands for every estate we tend<sup>®</sup></div>
    </div>
  </div>
  <div class="card__contact">
    <div class="card__address">47 Finch Crescent<br>Marrowdale, 3291</div>
    <div><span class="dot"></span>corbeacon@mailvessel.net<br><span class="dot"></span>www.Coral-Beacon-Trust.org</div>
  </div>
  <div class="gold-band">ACN 582 914 306</div>
</section>

<section class="card card--back">
  <div class="brand">
    <span class="brand__mark"></span>
    <div class="brand__text">
      <div class="brand__name">Coral Beacon Pty Ltd.</div>
      <div class="brand__tagline">Steady hands for every estate we tend<sup>®</sup></div>
    </div>
  </div>
  <div class="card__url">www.Coral-Beacon-Trust.org</div>
</section>

</body>
</html>
```